Business card for dental office with laser therapy / dental facial esthetic

A simple logo which should signifies
Dentistry intraoral as primary and with extended extraoral cosmetic facial esthetic services ( regenerative skincare ) which enhance Beauty as whole .
Conservative high tech approach by using laser intraoral and extraoral limited to face and neck
Front Face :May be black background with neon blue / purplish Rim signifies laser ( ?) & abstract face profile and tooth or Apple design in one ? / see upload inspiration design
Back side : simple appointment slots with date and time / white background / black letter

Color : black/ neon blue/ purplish and gold incorporate for logo design
Final design : dental / esthetic / modern high tech and safe

Target Market(s)

Dental Patients who seeks more high end cosmetic treatment

Industry/Entity Type

Health Care

Contact Information for Business Card

Esthetic modern elegant looking
Logo and office must haves important informations

Logo Text

Family & Cosmetic Dentistry

Font styles to use
Script

Requirements
Must have
• Name of practice and all important informations
• Family & Cosmetic Dentistry
• Lan B. Okafor DMD,PC
• 38412 Brantley Court ,ste.207
• Cedar Hollow ,VA 20391
• Ph. 703-555-0187
• Fax 703-5550193
Nice to have
• More abstract
• Front : black back ground with neon blue rim (signifies laser therapy)
• Logo can also be golden gold / neon blue
• Address & Infos can be white
Should not have
• Not to busy looking

```html
<!DOCTYPE html>
<html lang="en">
<head>
<meta charset="utf-8">
<title>Lan B. Okafor DMD,PC — Business Card</title>
<link rel="stylesheet" href="https://fonts.googleapis.com/css2?family=Playfair+Display:wght@500&family=Barlow+Semi+Condensed:wght@500;600&family=Great+Vibes&display=swap">
<style>
  :root {
    --stage: #cccccc;
    --black: #0a0a0d;
    --panel: #121218;
    --neon-blue: #19c3ff;
    --neon-purple: #8b5cff;
    --gold: #d4af37;
    --white: #ffffff;
    --ink: #111111;
  }
  html, body {
    margin: 0;
    padding: 0;
    width: 1096px;
    height: 1200px;
    overflow: hidden;
    background: var(--stage);
  }
  .card {
    position: absolute;
    left: 179px;
    width: 741px;
    height: 423px;
    overflow: hidden;
  }
  .card--front { top: 139px; background: var(--black); }
  .card--back { top: 639px; background: var(--white); }
  .card__shapes { position: absolute; inset: 0; width: 741px; height: 423px; }

  .brand-mark {
    position: absolute;
    display: flex;
    align-items: center;
    justify-content: center;
    border-radius: 50%;
    background: var(--gold);
    color: var(--black);
    font-family: "Barlow Semi Condensed", sans-serif;
    font-weight: 600;
    text-align: center;
    line-height: 1.05;
  }
  .card--front .brand-mark { left: 42px; top: 41px; width: 132px; height: 132px; font-size: 22px; }
  .card--back .brand-mark { left: 501px; top: 28px; width: 174px; height: 174px; font-size: 29px; }

  .practice-name {
    position: absolute;
    left: 296px;
    top: 104px;
    margin: 0;
    font-family: "Playfair Display", serif;
    font-weight: 500;
    font-size: 36px;
    letter-spacing: 2px;
    color: var(--gold);
    text-transform: uppercase;
    white-space: nowrap;
    transform: scaleX(0.86);
    transform-origin: left center;
  }
  .practice-tagline {
    position: absolute;
    left: 300px;
    top: 160px;
    margin: 0;
    font-family: "Great Vibes", cursive;
    font-size: 30px;
    color: var(--neon-blue);
    white-space: nowrap;
  }
  .contact {
    position: absolute;
    left: 287px;
    top: 256px;
    margin: 0;
    padding: 0;
    list-style: none;
    font-family: "Barlow Semi Condensed", sans-serif;
    font-weight: 500;
    font-size: 24px;
    line-height: 30px;
    color: var(--white);
  }
  .contact__item { display: flex; align-items: flex-start; }
  .contact__icon { width: 23px; height: 23px; margin: 4px 14px 0 0; flex: none; }
  .contact__text { white-space: nowrap; }

  .appointment-title {
    position: absolute;
    left: 54px;
    top: 194px;
    margin: 0;
    font-family: "Playfair Display", serif;
    font-weight: 500;
    font-size: 34px;
    color: var(--ink);
    transform: scaleX(0.88);
    transform-origin: left center;
  }
  .slot { position: absolute; top: 253px; width: 173px; }
  .slot--date { left: 52px; }
  .slot--time { left: 242px; }
  .slot__label {
    display: block;
    height: 25px;
    font-family: "Playfair Display", serif;
    font-weight: 500;
    font-size: 22px;
    line-height: 22px;
    color: var(--ink);
    padding-left: 2px;
    transform: scaleX(0.9);
    transform-origin: left center;
  }
  .slot__box {
    display: block;
    box-sizing: border-box;
    width: 173px;
    height: 59px;
    background: var(--white);
    border: 1.5px solid var(--ink);
  }
  .card__footer-band {
    position: absolute;
    left: 0;
    bottom: 0;
    width: 741px;
    height: 47px;
    background: var(--black);
    border-top: 3px solid var(--neon-blue);
    box-sizing: border-box;
  }
</style>
</head>
<body>

<section class="card card--front" aria-label="Business card front">
  <svg class="card__shapes" viewBox="0 0 741 423" aria-hidden="true">
    <rect width="741" height="423" fill="var(--black)"/>
    <path d="M287,0 Q150,200 147,423 L671,423 Q772,250 729,0 Z" fill="var(--neon-purple)"/>
    <path d="M293,0 Q170,210 178,423 L669,423 Q756,240 711,0 Z" fill="var(--neon-blue)"/>
    <path d="M296,0 Q195,210 212,423 L668,423 Q740,230 695,0 Z" fill="var(--panel)"/>
  </svg>

  <div class="brand-mark">Okafor<br>Dental</div>

  <h1 class="practice-name">Lan B. Okafor DMD,PC</h1>
  <p class="practice-tagline">Family &amp; Cosmetic Dentistry</p>

  <ul class="contact">
    <li class="contact__item">
      <svg class="contact__icon" viewBox="0 0 24 24" aria-hidden="true">
        <circle cx="12" cy="12" r="12" fill="var(--neon-blue)"/>
        <path d="M12 5.5a4.5 4.5 0 0 0-4.5 4.5c0 3.2 4.5 8.5 4.5 8.5s4.5-5.3 4.5-8.5A4.5 4.5 0 0 0 12 5.5z" fill="var(--black)"/>
        <circle cx="12" cy="10" r="1.7" fill="var(--neon-blue)"/>
      </svg>
      <span class="contact__text">38412 Brantley Court ,ste.207<br>Cedar Hollow ,VA 20391</span>
    </li>
    <li class="contact__item">
      <svg class="contact__icon" viewBox="0 0 24 24" aria-hidden="true">
        <circle cx="12" cy="12" r="12" fill="var(--neon-blue)"/>
        <path d="M8.2 6.2l2 2.4-1.2 1.6c.8 1.8 2.3 3.3 4.1 4.1l1.6-1.2 2.4 2-1.3 2.1c-4.5-.6-8.6-4.7-9.2-9.2z" fill="var(--black)"/>
      </svg>
      <span class="contact__text">Ph. 703-555-0187</span>
    </li>
    <li class="contact__item">
      <svg class="contact__icon" viewBox="0 0 24 24" aria-hidden="true">
        <circle cx="12" cy="12" r="12" fill="var(--neon-blue)"/>
        <rect x="8.5" y="5.5" width="7" height="4" fill="none" stroke="var(--black)" stroke-width="1.3"/>
        <rect x="6" y="9.5" width="12" height="6" rx="1" fill="none" stroke="var(--black)" stroke-width="1.3"/>
        <rect x="8.5" y="13.5" width="7" height="4" fill="var(--neon-blue)" stroke="var(--black)" stroke-width="1.3"/>
      </svg>
      <span class="contact__text">Fax 703-5550193</span>
    </li>
  </ul>
</section>

<section class="card card--back" aria-label="Business card back">
  <div class="brand-mark">Okafor<br>Dental</div>

  <h2 class="appointment-title">APPOINTMENT</h2>

  <div class="slot slot--date">
    <span class="slot__label">DATE</span>
    <span class="slot__box"></span>
  </div>
  <div class="slot slot--time">
    <span class="slot__label">TIME</span>
    <span class="slot__box"></span>
  </div>

  <div class="card__footer-band"></div>
</section>

</body>
</html>
```